Wealth management firm needs a business card design

Using my logo, create a business card that covers all of the regulatory wordings that I need. It must have - Registered Office 7-9 Pelgrove Wynd, Edinburgh, EH4 2QN. Registered in Scotland under number SC804317. VORELT Wealth Management Ltd is an appointed representative of Kestoby wealth management Ltd, which is authorised and regulated by the Monetary Oversight Council.

Target Market(s)

professional clients

Industry/Entity Type

finance

Contact Information for Business Card

VORELT Wealth Management, Conor Tresk-Whitlaw, Director, 5 Dunmore Row, Edinburgh, EH9 4RT. 07812 459 163, conor.tresk-whitlaw@vorelt-example.com , www.vorelt-example.com

Font styles to use
Serif

Colors
0054AA
0677BA
7BADD7
CADEEF
E8F1F8

Requirements
Must have
• regulatory wording in small text at bottom

```html
<!DOCTYPE html>
<html lang="en">
<head>
<meta charset="utf-8">
<title>VORELT Wealth Management – Business Card</title>
<link rel="stylesheet" href="https://fonts.googleapis.com/css2?family=Tinos:wght@400;700&family=Open+Sans:wght@400;600&display=swap">
<style>
  :root {
    --navy: #0054AA;
    --blue: #0677BA;
    --sky: #7BADD7;
    --mist: #CADEEF;
    --ice: #E8F1F8;
    --ink: #1c1c1c;
    --grey: #555b61;
    --backdrop: #e6e7e9;
    --card: #ffffff;
  }
  * { margin: 0; padding: 0; box-sizing: border-box; }
  html, body { width: 900px; height: 1200px; overflow: hidden; }
  body {
    background: var(--backdrop);
    position: relative;
    font-family: "Open Sans", Arial, sans-serif;
  }
  .card {
    position: absolute;
    left: 110px;
    width: 680px;
    height: 440px;
    background: var(--card);
    box-shadow: 0 6px 18px rgba(0,0,0,0.18);
  }
  .card--front { top: 140px; }
  .card--back { top: 640px; }

  /* Front */
  .brand {
    position: absolute;
    top: 120px;
    left: 0;
    right: 0;
    text-align: center;
  }
  .brand__mark {
    display: block;
    width: 62px;
    height: 62px;
    margin: 0 auto 18px;
    border-radius: 50%;
    background: var(--blue);
  }
  .brand__name {
    font-family: "Tinos", "Times New Roman", serif;
    font-size: 34px;
    font-weight: 400;
    color: var(--ink);
    letter-spacing: 0.2px;
  }
  .brand__tagline {
    font-family: "Tinos", "Times New Roman", serif;
    font-size: 12px;
    color: var(--ink);
    margin-top: 4px;
    padding-left: 150px;
  }
  .regulatory {
    position: absolute;
    left: 56px;
    right: 56px;
    top: 300px;
    font-family: "Tinos", "Times New Roman", serif;
    font-size: 9.5px;
    line-height: 1.45;
    color: var(--ink);
    text-align: justify;
  }

  /* Back */
  .back-brand {
    position: absolute;
    top: 44px;
    right: 52px;
    font-family: "Tinos", "Times New Roman", serif;
    font-size: 30px;
    color: var(--blue);
    letter-spacing: 1px;
  }
  .contact {
    position: absolute;
    left: 36px;
    top: 218px;
    color: var(--grey);
  }
  .contact__name {
    font-size: 24px;
    font-weight: 600;
    color: var(--blue);
  }
  .contact__role {
    font-size: 13px;
    color: var(--ink);
    padding-bottom: 4px;
    border-bottom: 1.5px solid var(--blue);
    display: inline-block;
    width: 42px;
    white-space: nowrap;
  }
  .contact__lines { margin-top: 22px; font-size: 13px; line-height: 1.75; }
  .contact__lines .gap { margin-top: 8px; }
  .contact__address { color: var(--blue); font-weight: 600; }
</style>
</head>
<body>
  <section class="card card--front" aria-label="Card front">
    <div class="brand">
      <span class="brand__mark" aria-hidden="true"></span>
      <div class="brand__name">VORELT Wealth Management Ltd</div>
      <div class="brand__tagline">Personal Financial Advice</div>
    </div>
    <p class="regulatory">Registered Office 7-9 Pelgrove Wynd, Edinburgh, EH4 2QN. Registered in Scotland under number SC804317. VORELT Wealth Management Ltd is an appointed representative of Kestoby wealth management Ltd, which is authorised and regulated by the Monetary Oversight Council.</p>
  </section>

  <section class="card card--back" aria-label="Card back">
    <div class="back-brand">VORELT</div>
    <div class="contact">
      <div class="contact__name">Conor Tresk-Whitlaw</div>
      <div class="contact__role">Director</div>
      <div class="contact__lines">
        <div>07812 459 163</div>
        <div>www.vorelt-example.com</div>
        <div class="gap">conor.tresk-whitlaw@vorelt-example.com</div>
        <div class="contact__address">5 Dunmore Row, Edinburgh, EH9 4RT.</div>
      </div>
    </div>
  </section>
</body>
</html>
```